Billboard design 8x3M NURA (Spanish company)

We´re located in the south of Spain. We run a local telecom company.
We sell Fiber optic, and mobile phone lines mainly.
The billboard will have to be in Spanish, I would like the price to be something you spot on first sight when passing by in the car.
Our company color is blue, like in our logo which I will add. I will also add a example from what we currently have.
The new offer should be:
1000 megas + 100Gigas movil con llamadas ilimitadas. (meaning 1000Mb fiber optic speed and 100Gb data and unlimited calls for 1 mobile line)
Our details are: phone line 952 00 0147
Website: nu-ra.es

```html
<!DOCTYPE html>
<html lang="es">
<head>
<meta charset="utf-8">
<title>NURA – Valla 1000 Megas</title>
<link rel="stylesheet" href="https://fonts.googleapis.com/css2?family=Montserrat:wght@600;700;800;900&family=Anton&display=swap">
<style>
  :root {
    --backdrop: #232b31;
    --navy: #16384f;
    --blue-deep: #1c4a66;
    --blue-mid: #1f6a9a;
    --blue-bright: #2a8fd6;
    --band: #1e7fcc;
    --orange: #fbae24;
    --orange-dark: #f39a10;
    --white: #ffffff;
    --ink: #14283a;
  }
  * { margin: 0; padding: 0; box-sizing: border-box; }
  html, body { width: 1200px; height: 544px; overflow: hidden; background: var(--backdrop); }
  body { position: relative; font-family: "Montserrat", Arial, sans-serif; }

  .billboard {
    position: absolute; left: 102px; top: 75px; width: 997px; height: 374px;
    overflow: hidden;
    background: linear-gradient(100deg, var(--blue-deep) 0%, var(--blue-mid) 45%, var(--blue-bright) 100%);
    box-shadow: 0 10px 24px rgba(0,0,0,.45);
  }
  .offer-band {
    position: absolute; left: 0; top: 151px; width: 667px; height: 56px;
    background: linear-gradient(90deg, #1b6fb2 0%, var(--band) 70%, #2b9ae6 100%);
  }
  .hero-visual {
    position: absolute; left: 592px; top: 37px; width: 405px; height: 337px;
    background:
      radial-gradient(ellipse at 48% 55%, #cfe6ff 0%, #5fb0ef 18%, rgba(42,122,190,.6) 45%, rgba(30,90,150,0) 75%),
      linear-gradient(180deg, #1e6fae 0%, #17406a 60%, #2a7fc0 100%);
    border-radius: 40px 0 0 0;
  }

  .speed {
    position: absolute; left: 40px; top: 28px;
    color: var(--orange); font-weight: 800; font-size: 142px; line-height: 1; letter-spacing: -4px;
  }
  .plan-lines {
    position: absolute; left: 380px; top: 38px; color: var(--white);
    font-weight: 800; line-height: 0.82; font-size: 59px; letter-spacing: -1px;
  }
  .offer-text {
    position: absolute; left: 41px; top: 155px; color: var(--white);
    font-weight: 700; font-size: 40px; letter-spacing: -0.3px; line-height: 1.2;
  }

  .brand { position: absolute; left: 47px; top: 240px; color: var(--white); }
  .brand-name { font-weight: 900; font-size: 74px; line-height: 1; letter-spacing: 2px; }
  .brand-services { margin-top: 10px; font-weight: 600; font-size: 21px; letter-spacing: -0.2px; }

  .contact {
    position: absolute; left: 329px; width: 247px; height: 41px; border-radius: 21px;
    display: flex; align-items: center; gap: 8px; padding-left: 4px;
    font-weight: 800; color: var(--ink);
  }
  .contact-phone { top: 241px; background: var(--white); font-size: 29px; }
  .contact-web { top: 294px; background: var(--orange); font-size: 27px; }
  .contact-icon {
    width: 31px; height: 31px; border-radius: 50%; flex: none;
    display: flex; align-items: center; justify-content: center; background: var(--orange);
  }
  .contact-web .contact-icon { background: var(--white); }

  .price-badge { position: absolute; left: 833px; top: 0; width: 114px; height: 137px; }
  .price-label {
    position: absolute; left: 833px; top: 26px; width: 114px; text-align: center;
    color: var(--ink); font-weight: 800; font-size: 15px;
  }
  .price-amount {
    position: absolute; left: 833px; top: 40px; width: 114px; text-align: center;
    color: var(--navy); font-family: "Anton", Impact, sans-serif; font-size: 66px; line-height: 1.05;
  }
</style>
</head>
<body>
  <main class="billboard">
    <div class="hero-visual" role="img" aria-label="Cohete despegando desde la pantalla de un portátil entre nubes de humo, con una ciudad digital de fondo"></div>

    <div class="offer-band"></div>

    <div class="speed">1000</div>
    <div class="plan-lines">MEGAS<br>+ 100GIGAS</div>
    <div class="offer-text">Movil con llamadas ilimitadas</div>

    <div class="brand">
      <div class="brand-name">NURA</div>
      <div class="brand-services">Wifi | Fibra | Movil | Tv</div>
    </div>

    <div class="contact contact-phone">
      <span class="contact-icon">
        <svg width="14" height="20" viewBox="0 0 14 20" aria-hidden="true">
          <rect x="1.5" y="1" width="11" height="18" rx="2" fill="none" stroke="#fff" stroke-width="2"/>
          <circle cx="7" cy="15.5" r="1.2" fill="#fff"/>
        </svg>
      </span>
      952 00 0147
    </div>

    <div class="contact contact-web">
      <span class="contact-icon">
        <svg width="20" height="20" viewBox="0 0 20 20" aria-hidden="true" fill="none" stroke="#f39a10" stroke-width="1.6">
          <circle cx="10" cy="10" r="8"/>
          <ellipse cx="10" cy="10" rx="3.5" ry="8"/>
          <path d="M2 10h16M3.5 6h13M3.5 14h13"/>
        </svg>
      </span>
      www.nu-ra.es
    </div>

    <svg class="price-badge" viewBox="0 0 114 137" aria-hidden="true">
      <polygon points="2,0 112,0 112,106 57,135 2,106" fill="#fbae24" stroke="#16384f" stroke-width="3"/>
    </svg>
    <div class="price-label">ONLY</div>
    <div class="price-amount">35€</div>
  </main>
</body>
</html>
```